Bref créative
The Lanternfold
Come Together
I need double sided standard sized Business Card [3.5" x 2"]
Be creative, I would like to see some designs with the logo font but try other fonts
Professional
Corvin T. Ashby
Reverend
417 Maple Hollow Road
Fernbrook Vale, Oregon
cash@thelanternfoldmx.org
I also want a T-shirts designs (front and back) and some banner designs for the launchng of a church plant.
Just the logo or the lower case "g" in the logo

```html
<!DOCTYPE html>
<html lang="en">
<head>
<meta charset="utf-8">
<title>The Lanternfold — Stationery &amp; Apparel</title>
<link rel="stylesheet" href="https://fonts.googleapis.com/css2?family=Open+Sans:wght@400;600;700&display=swap">
<style>
  :root{
    --bg:#2e2f30;
    --paper:#ffffff;
    --green:#3f9a1a;
    --lime:#8cc63f;
    --deep:#1f5e0c;
    --yellow:#f2c200;
    --ink:#4a4a4a;
    --muted:#9a9a9a;
  }
  *{box-sizing:border-box;margin:0;padding:0}
  html,body{width:1200px;height:906px;overflow:hidden}
  body{background:var(--bg);font-family:"Open Sans",Arial,sans-serif;color:var(--ink);position:relative}
  .piece{position:absolute;background:var(--paper);overflow:hidden;box-shadow:0 4px 14px rgba(0,0,0,.45)}
  .swoosh{position:absolute;left:0;top:0;width:100%;display:block}
  .wordmark{font-weight:700;color:var(--green);white-space:nowrap;display:flex;align-items:center;gap:.4em}
  .wordmark .dot{width:.9em;height:.9em;border-radius:50%;background:var(--green);flex:none}
  .wordmark.on-dark{color:var(--paper)}
  .wordmark.on-dark .dot{background:var(--paper)}

  /* apparel prints */
  .shirt-print{top:30px;width:200px;height:290px}
  .shirt-print .chest{position:absolute;left:22px;top:40px;font-size:13px}
  .shirt-print .big-mark{position:absolute;border-radius:50%;background:radial-gradient(circle at 40% 35%,var(--lime),var(--green) 60%,var(--deep))}
  .shirt-print .back-name{position:absolute;left:0;right:0;bottom:40px;display:flex;justify-content:center;font-size:15px}
  .shirt-label{position:absolute;left:0;right:0;bottom:10px;text-align:center;font-size:10px;color:var(--muted);letter-spacing:.1em;text-transform:uppercase}

  /* letterhead */
  .letterhead{left:70px;top:400px;width:340px;height:460px}
  .letterhead .wordmark{position:absolute;left:26px;top:34px;font-size:16px}
  .letterhead .tagline{position:absolute;left:52px;top:56px;font-size:8px;color:var(--muted)}
  .letterhead .faint-mark{position:absolute;right:-40px;bottom:40px;width:200px;height:200px;border-radius:50%;background:rgba(63,154,26,.05)}
  .letterhead .footer{position:absolute;left:0;right:0;bottom:0;height:22px;background:var(--green);color:var(--paper);font-size:7.5px;display:flex;align-items:center;padding:0 16px;gap:14px;white-space:nowrap}

  /* business cards */
  .card{width:250px;height:143px}
  .card-front{left:440px;top:400px}
  .card-front .wordmark{position:absolute;left:14px;top:38px;font-size:13px}
  .card-front .address{position:absolute;left:14px;top:68px;font-size:8px;line-height:1.45}
  .card-front .person{position:absolute;right:14px;top:74px;text-align:right}
  .card-front .person strong{display:block;font-size:10.5px;color:var(--deep)}
  .card-front .person span{display:block;font-size:8px;color:var(--muted)}
  .card-front .email{position:absolute;right:14px;bottom:12px;font-size:7.5px;color:var(--green)}
  .card-back{left:710px;top:400px;background:radial-gradient(circle at 50% 50%,var(--lime),var(--green) 55%,var(--deep));display:flex;align-items:center;justify-content:center}
  .card-back .wordmark{font-size:15px}

  /* envelope */
  .envelope{left:440px;top:565px;width:390px;height:180px}
  .envelope .wordmark{position:absolute;left:18px;top:44px;font-size:14px}
  .envelope .return{position:absolute;left:38px;top:66px;font-size:8px;line-height:1.45}
  .envelope .faint-mark{position:absolute;right:30px;bottom:-30px;width:130px;height:130px;border-radius:50%;background:rgba(63,154,26,.06)}

  /* horizontal banner */
  .banner-wide{left:440px;top:765px;width:390px;height:95px;background:linear-gradient(100deg,var(--deep),var(--green) 45%,var(--lime));display:flex;align-items:center;justify-content:center;gap:14px}
  .banner-wide .wordmark{font-size:20px}
  .banner-wide .slogan{color:var(--yellow);font-size:11px;font-weight:600;letter-spacing:.12em;text-transform:uppercase}

  /* flyer */
  .flyer{left:850px;top:565px;width:185px;height:295px}
  .flyer .hero{position:absolute;left:0;top:0;width:100%;height:120px;background:radial-gradient(circle at 50% 45%,var(--lime),var(--green) 60%,var(--deep))}
  .flyer .wordmark{position:absolute;left:12px;top:132px;font-size:11px}
  .flyer h2{position:absolute;left:12px;top:156px;font-size:13px;color:var(--green);font-weight:700}
  .flyer p{position:absolute;left:12px;right:12px;top:178px;font-size:7.5px;line-height:1.5}
  .flyer .photo{position:absolute;right:12px;bottom:12px;width:70px;height:46px;background:linear-gradient(135deg,#d9e8c8,#a9c98a)}

  /* vertical banner */
  .banner-tall{left:1055px;top:360px;width:115px;height:500px}
  .banner-tall .top{position:absolute;left:0;top:0;width:100%;height:300px;background:linear-gradient(180deg,var(--deep),var(--green) 50%,var(--lime))}
  .banner-tall .top .disc{position:absolute;left:27px;top:110px;width:60px;height:60px;border-radius:50%;background:var(--paper);opacity:.9}
  .banner-tall .wordmark{position:absolute;left:10px;bottom:46px;font-size:10px}
  .banner-tall .slogan{position:absolute;left:10px;bottom:28px;font-size:8px;color:var(--muted)}
</style>
</head>
<body>

  <!-- apparel prints -->
  <section class="piece shirt-print" style="left:40px">
    <div class="wordmark chest"><span class="dot"></span>The Lanternfold</div>
    <div class="big-mark" style="left:40px;top:100px;width:120px;height:120px"></div>
    <div class="shirt-label">Front</div>
  </section>
  <section class="piece shirt-print" style="left:270px">
    <div class="big-mark" style="left:35px;top:50px;width:130px;height:130px"></div>
    <div class="wordmark back-name">The Lanternfold</div>
    <div class="shirt-label">Back</div>
  </section>
  <section class="piece shirt-print" style="left:500px">
    <div class="big-mark" style="left:70px;top:60px;width:60px;height:60px"></div>
    <div class="shirt-label">Front</div>
  </section>
  <section class="piece shirt-print" style="left:730px">
    <div class="big-mark" style="left:75px;top:50px;width:50px;height:50px"></div>
    <div class="wordmark back-name">The Lanternfold</div>
    <div class="shirt-label">Back</div>
  </section>
  <section class="piece shirt-print" style="left:960px">
    <div class="wordmark chest" style="left:40px;top:120px;font-size:14px"><span class="dot"></span>The Lanternfold</div>
    <div class="shirt-label">Front</div>
  </section>

  <!-- letterhead -->
  <section class="piece letterhead">
    <svg class="swoosh" viewBox="0 0 100 20" preserveAspectRatio="none" height="24">
      <path d="M0 0H100V9C70 18 30 6 0 14Z" fill="var(--yellow)"/>
      <path d="M0 0H100V6C70 14 30 3 0 10Z" fill="var(--green)"/>
    </svg>
    <div class="wordmark"><span class="dot"></span>The Lanternfold</div>
    <div class="tagline">Come Together</div>
    <div class="faint-mark"></div>
    <div class="footer"><span>417 Maple Hollow Road, Fernbrook Vale, Oregon</span><span>cash@thelanternfoldmx.org</span></div>
  </section>

  <!-- business card front -->
  <section class="piece card card-front">
    <svg class="swoosh" viewBox="0 0 100 20" preserveAspectRatio="none" height="26">
      <path d="M0 0H100V10C70 19 30 6 0 15Z" fill="var(--yellow)"/>
      <path d="M0 0H100V7C70 15 30 3 0 11Z" fill="var(--green)"/>
    </svg>
    <div class="wordmark"><span class="dot"></span>The Lanternfold</div>
    <div class="address">417 Maple Hollow Road<br>Fernbrook Vale, Oregon</div>
    <div class="person"><strong>Corvin T. Ashby</strong><span>Reverend</span></div>
    <div class="email">cash@thelanternfoldmx.org</div>
  </section>

  <!-- business card back -->
  <section class="piece card card-back">
    <div class="wordmark on-dark"><span class="dot"></span>The Lanternfold</div>
  </section>

  <!-- envelope -->
  <section class="piece envelope">
    <svg class="swoosh" viewBox="0 0 100 20" preserveAspectRatio="none" height="30">
      <path d="M0 0H100V10C70 19 30 6 0 15Z" fill="var(--yellow)"/>
      <path d="M0 0H100V7C70 15 30 3 0 11Z" fill="var(--green)"/>
    </svg>
    <div class="wordmark"><span class="dot"></span>The Lanternfold</div>
    <div class="return">417 Maple Hollow Road<br>Fernbrook Vale, Oregon</div>
    <div class="faint-mark"></div>
  </section>

  <!-- wide banner -->
  <section class="piece banner-wide">
    <div class="wordmark on-dark"><span class="dot"></span>The Lanternfold</div>
    <div class="slogan">Come Together</div>
  </section>

  <!-- flyer -->
  <section class="piece flyer">
    <div class="hero"></div>
    <div class="wordmark"><span class="dot"></span>The Lanternfold</div>
    <h2>Lorem ipsum</h2>
    <p>Join us as we open our doors to the neighborhood. Bring your family and friends for an evening of worship, music, food and fellowship together.</p>
    <div class="photo" role="img" aria-label="Photo of the congregation gathering"></div>
  </section>

  <!-- tall banner -->
  <section class="piece banner-tall">
    <div class="top"><div class="disc"></div></div>
    <div class="wordmark"><span class="dot"></span>The Lanternfold</div>
    <div class="slogan">Come Together</div>
  </section>

</body>
</html>
```